Re-design a website for a millionaire mentor

We need an expert website designer to re-design the website vKeenstride.net

The website would have 4 pages. A home page, Summit Circle page, Hire RM page and an About page.

Here are some reference websites

https://www.lumovance.net
https://rolfbanter.net/

I will also attach a beginning of mockup of the home page I did myself to give an idea of the style we like, please use the quote "If you are not chasing your potential you are wasting your life" instead of the one in the current website...

You don't have the use the mockup (just the quote) and are free to use all your creativity.

Target Market(s)

Entrepreneurs

Number of Pages Required

4 page

Font styles to use
Other font styles liked:
• Franklin Gothic

Requirements
Must have
• -Call of action on the main page to download a free business plan
• -Hire rm page check out reference: http://www.hiremarkbellow.net
• -summit circle page with a button to sign in or join the summit circle. Check out reference for example: https://www.lumovance.net/glide_academy

```html
<!DOCTYPE html>
<html lang="en">
<head>
<meta charset="utf-8">
<title>Hire RM — Keen Stride</title>
<link href="https://fonts.googleapis.com/css2?family=Libre+Franklin:wght@400;500;600;700&family=Mulish:wght@400;600&display=swap" rel="stylesheet">
<style>
:root{
  --red:#e3262b;
  --red-dark:#b5161a;
  --ink:#1b1b1b;
  --label:#333;
  --muted:#8a8a8a;
  --field-line:#cfcfcf;
  --footer:#161616;
  --footer-line:#2c2c2c;
  --white:#fff;
}
*{box-sizing:border-box;margin:0;padding:0}
html,body{width:1200px;height:3475px;overflow:hidden;background:var(--white)}
body{position:relative;font-family:"Mulish",sans-serif;color:var(--ink)}
.abs{position:absolute}

/* header */
.hero{left:0;top:0;width:1200px;height:417px;background:linear-gradient(180deg,#3a3a3a 0%,#2a2a2a 55%,#3b3326 100%);overflow:hidden}
.hero-photo{right:0;top:0;width:470px;height:417px;background:radial-gradient(ellipse at 55% 55%,#232a33 0%,#141618 55%,rgba(20,20,20,0) 80%)}
.brand{display:flex;align-items:flex-start;gap:8px}
.brand-dot{width:22px;height:22px;border-radius:50%;background:var(--red);margin-top:6px;flex:none}
.brand-name{font-family:"Libre Franklin",sans-serif;font-weight:700;color:var(--white);letter-spacing:1px;line-height:1.05;display:block}
.header-brand{left:81px;top:16px}
.header-brand .brand-name{font-size:30px}
.nav{left:598px;top:36px;font-family:"Libre Franklin",sans-serif;font-size:16px;color:var(--white)}
.nav a{color:inherit;text-decoration:none;position:absolute;white-space:nowrap}
.nav .current{color:var(--red)}
.login{left:1008px;top:23px;width:116px;height:46px;border-radius:23px;background:linear-gradient(180deg,#f0353a,var(--red-dark));color:var(--white);font-family:"Libre Franklin",sans-serif;font-weight:600;font-size:19px;display:flex;align-items:center;justify-content:center}
.page-title{left:81px;top:205px;font-family:"Libre Franklin",sans-serif;font-weight:500;font-size:56px;color:var(--white)}

/* intro */
.form-title{left:0;width:1200px;top:498px;text-align:center;font-family:"Libre Franklin",sans-serif;font-weight:500;font-size:42px;color:#111}
.form-sub{left:240px;width:720px;top:562px;text-align:center;font-family:"Libre Franklin",sans-serif;font-size:29px;line-height:47px;color:#111}
.help{left:0;width:1200px;top:664px;text-align:center;font-size:15px;color:var(--red)}

/* fields */
.field{height:46px;border:2px solid var(--field-line);border-radius:23px;padding:0 18px;font-size:13px;color:#666;display:flex;align-items:center}
.area{border:2px solid var(--field-line);border-radius:14px;padding:14px 18px;font-size:13px;color:#666}
.full{left:248px;width:704px}
.left{left:248px;width:343px}
.right{left:609px;width:343px}
.q{left:250px;font-family:"Libre Franklin",sans-serif;font-weight:600;font-size:16px;line-height:20px;color:var(--label)}
.opt{font-size:13px;line-height:16px;color:#444;display:flex;align-items:center;gap:10px}
.opt::before{content:"";width:13px;height:13px;border:1.5px solid #444;border-radius:50%}
.c1{left:250px}.c2{left:510px}.c3{left:748px}

.submit{left:480px;top:2861px;width:238px;height:50px;border-radius:25px;background:linear-gradient(180deg,#f0353a,var(--red-dark));color:var(--white);font-family:"Libre Franklin",sans-serif;font-size:20px;display:flex;align-items:center;justify-content:center}
.note{left:215px;width:770px;top:2934px;text-align:center;font-size:14px;line-height:21px;color:#a9a9a9}

/* footer */
.footer{left:0;top:3079px;width:1200px;height:396px;background:var(--footer)}
.footer-brand{left:104px;top:3128px}
.footer-brand .brand-name{font-size:36px}
.footer-brand .brand-dot{width:26px;height:26px;margin-top:8px}
.social{top:3255px;width:38px;height:38px;border-radius:50%;background:#1e6fd0}
.f-head{top:3113px;font-family:"Libre Franklin",sans-serif;font-weight:600;font-size:16px;color:var(--white)}
.sitemap{left:348px;top:3148px;list-style:none;font-size:15px;color:#ddd;line-height:31px}
.sitemap li::before{content:"";display:inline-block;width:6px;height:6px;background:var(--red);border-radius:50%;margin-right:14px;vertical-align:middle}
.contact{left:614px;font-size:15px;color:#ddd;display:flex;gap:14px;line-height:22px}
.contact svg{flex:none;margin-top:2px}
.map{left:906px;top:3153px;width:172px;height:172px;border-radius:50%;background:radial-gradient(circle at 50% 45%,#f5f1e8 0%,#e9e4d8 70%,#d9d3c5 100%);border:3px solid #fff}
.rule{left:104px;top:3360px;width:992px;height:1px;background:var(--footer-line)}
.copy{left:0;width:1200px;top:3388px;text-align:center;font-size:13px;color:#ddd}
</style>
</head>
<body>

<header class="abs hero">
  <div class="abs hero-photo" role="img" aria-label="Photo of the mentor seen from behind, looking over a city at dusk"></div>
</header>
<div class="abs brand header-brand"><span class="brand-dot"></span><span class="brand-name">KEEN<br>STRIDE</span></div>
<nav class="abs nav">
  <a style="left:0">HOME</a>
  <a style="left:79px">SUMMIT CIRCLE</a>
  <a class="current" style="left:229px">HIRE RM</a>
  <a style="left:331px">ABOUT</a>
</nav>
<div class="abs login">LOGIN</div>
<h1 class="abs page-title">HIRE RM</h1>

<h2 class="abs form-title">REID MALONE &amp; ASSOCIATES CLIENT FORM</h2>
<p class="abs form-sub">Please complete the form below to request for REID MALONE to be a part of your event.</p>
<p class="abs help">If you need help please call: 866-555-0142 ext.</p>

<div class="abs field left" style="top:732px">First Name *</div>
<div class="abs field right" style="top:732px">Last Name *</div>
<div class="abs field left" style="top:799px">Email *</div>
<div class="abs field right" style="top:799px">Phone *</div>
<div class="abs field full" style="top:866px">Company *</div>
<div class="abs field left" style="top:934px">Company Address *</div>
<div class="abs field right" style="top:934px">Company City *</div>
<div class="abs field left" style="top:1001px">Company State *</div>
<div class="abs field right" style="top:1001px">Company Zip *</div>
<div class="abs area full" style="top:1070px;height:119px">Event Date(s) of Interest *</div>

<div class="abs q" style="top:1209px">Organization Type *</div>
<div class="abs opt c1" style="top:1243px">Middle School</div>
<div class="abs opt c2" style="top:1243px">High School</div>
<div class="abs opt c3" style="top:1243px">College/University</div>
<div class="abs opt c1" style="top:1273px">Non-Profit - Religious</div>
<div class="abs opt c2" style="top:1273px">Non-Profit - Non-Religious</div>
<div class="abs opt c3" style="top:1273px">Corporate</div>

<div class="abs q" style="top:1334px">Projected Budget for Securing Services *</div>
<div class="abs opt c1" style="top:1368px">$10-20K</div>
<div class="abs opt c2" style="top:1368px">$20-30K</div>
<div class="abs opt c3" style="top:1368px">$30-40K</div>
<div class="abs opt c1" style="top:1398px">$40-50K</div>
<div class="abs opt c2" style="top:1398px">$50K Plus</div>

<div class="abs field full" style="top:1450px">Venue - Name of Facility *</div>
<div class="abs area full" style="top:1518px;height:118px">Venue Address/Location - Include the Closest Airport(s). *</div>
<div class="abs field full" style="top:1659px">Event Name *</div>
<div class="abs area full" style="top:1726px;height:118px">Purpose of Event *</div>
<div class="abs field full" style="top:1867px">Event Time *</div>
<div class="abs area full" style="top:1935px;height:118px">Topic Chosen for Presentation *</div>
<div class="abs area full" style="top:2076px;height:116px">What time(s) do the session(s) begin and what are the requested duration(s)? *</div>

<div class="abs q" style="top:2219px">Planned Number of People Attending *</div>
<div class="abs opt c1" style="top:2253px">Under 500</div>
<div class="abs opt c2" style="top:2253px">500-1000</div>
<div class="abs opt c3" style="top:2253px">1000-3000</div>
<div class="abs opt c1" style="top:2286px">3000-5000</div>
<div class="abs opt c2" style="top:2286px">5000 Plus</div>
<div class="abs area full" style="top:2333px;height:116px">Event Attendee Demographics *</div>

<div class="abs q" style="top:2476px">Will This Event Be Open To The Public? *</div>
<div class="abs opt c1" style="top:2512px">Yes</div>
<div class="abs opt c2" style="top:2512px">No</div>
<div class="abs q" style="top:2560px">Will Tickets Be Sold For This Event? - Ticket sales must be approved by RMA. *</div>
<div class="abs opt c1" style="top:2595px">Yes</div>
<div class="abs opt c2" style="top:2595px">No</div>
<div class="abs q" style="top:2638px">Do You Intend To Record Or Live Stream This Event? *</div>
<div class="abs opt c1" style="top:2674px">Yes</div>
<div class="abs opt c2" style="top:2674px">No</div>
<div class="abs q" style="top:2722px">Can Products Be Sold At This Event? *</div>
<div class="abs opt c1" style="top:2757px">Yes</div>
<div class="abs opt c2" style="top:2757px">No</div>

<div class="abs field left" style="top:2794px">Event Contact Name *</div>
<div class="abs field right" style="top:2794px">Event Contact Details *</div>

<div class="abs submit">REQUEST EVENT</div>
<p class="abs note">RMA does not hold dates for non-committal inquiries. RMA will TEMPORARILY hold dates once a FULLY executed agreement has been reached as evidenced by a signed contract with both signatures. Dates are NOT reserved until you have received confirmation that your deposit has been received.</p>

<footer class="abs footer"></footer>
<div class="abs brand footer-brand"><span class="brand-dot"></span><span class="brand-name">KEEN<br>STRIDE</span></div>
<span class="abs social" style="left:122px"></span>
<span class="abs social" style="left:171px"></span>
<span class="abs social" style="left:217px"></span>
<span class="abs social" style="left:264px"></span>

<div class="abs f-head" style="left:348px">SITEMAP</div>
<ul class="abs sitemap">
  <li>Home</li><li>Summit Circle</li><li>Hire RM</li><li>About</li>
</ul>

<div class="abs f-head" style="left:614px">CONTACT US</div>
<div class="abs contact" style="top:3150px">
  <svg width="16" height="22" viewBox="0 0 16 22"><path d="M8 0a8 8 0 0 0-8 8c0 6 8 14 8 14s8-8 8-14a8 8 0 0 0-8-8z" fill="var(--red)"/><circle cx="8" cy="8" r="3" fill="var(--footer)"/></svg>
  <span>210 Larkmoor Ave Suite<br>#118 Harlow, DC 20009</span>
</div>
<div class="abs contact" style="top:3230px">
  <svg width="18" height="18" viewBox="0 0 24 24"><path d="M6.6 10.8a15 15 0 0 0 6.6 6.6l2.2-2.2a1 1 0 0 1 1-.25 11.4 11.4 0 0 0 3.6.57 1 1 0 0 1 1 1V20a1 1 0 0 1-1 1A17 17 0 0 1 3 4a1 1 0 0 1 1-1h3.5a1 1 0 0 1 1 1c0 1.250.2 2.45.57 3.6a1 1 0 0 1-.25 1z" fill="var(--red)"/></svg>
  <span style="font-size:17px">+1 866 555 0190</span>
</div>
<div class="abs contact" style="top:3274px">
  <svg width="18" height="14" viewBox="0 0 18 14"><rect width="18" height="14" rx="2" fill="var(--red)"/><path d="M1 2l8 6 8-6" stroke="var(--footer)" stroke-width="1.6" fill="none"/></svg>
  <span>info@vKeenstride.net</span>
</div>

<div class="abs f-head" style="left:873px">LOCATION MAP</div>
<div class="abs map" role="img" aria-label="Street map around the office with a location pin"></div>

<div class="abs rule"></div>
<p class="abs copy">©vKeenstride - 2019 All Right Reserved. Privacy Policy | Disclaimer | Refund Policy</p>

</body>
</html>
```